Kestrel Plumbing business card full re design & logo design

Kestrel Plumbing is a Sydney based mechanical plumbing contractor company.
We would like a full redesign with new logo etc which we can take to a future website, uniforms, vehicle sign writing etc.
Blue is my preferred choice of colour but i would be open to see a couple of alternatives thrown in the mix to see how they compare. I am open to see on white cards, black cards etc. Open to many new ideas.
Please see attached original business cards which have been used for the last 5 years.

Target Market(s)

Mechanical services industry.

Industry/Entity Type

Plumbing

Contact Information for Business Card

Dale Fenmore
Director

Mob: 0427 596 418
Email: dale@kestrelplumbing-demo.net.au
PO BOX 782
Carrowbrook NSW 2179
Lic: 518604k

Logo Text

Kestrel Plumbing

Font styles to use
Sans Serif

Colors
0655a3
3276b5
0792cd
33a6d7
85cae6
000000
333333
474747

Requirements
Must have
• Things that make it very professional and very well presented.
Nice to have
• Same description or very similar to attached uploaded file
Should not have
• Anything that makes it look unprofessional or cartoony.

```html
<!DOCTYPE html>
<html lang="en">
<head>
<meta charset="utf-8">
<title>Kestrel Plumbing – Business Card</title>
<link rel="stylesheet" href="https://fonts.googleapis.com/css2?family=Arimo:wght@400;700&family=Open+Sans:wght@400;700&display=swap">
<style>
  :root {
    --navy: #203063;
    --navy-deep: #1f2f62;
    --text-grey: #6b6b6b;
    --mark-muted: #7d7fa6;
    --white: #ffffff;
    --stage-dark: #000000;
    --stage-glow: #4a4a4a;
  }
  * { margin: 0; padding: 0; box-sizing: border-box; }
  html, body { width: 999px; height: 1200px; overflow: hidden; }
  body {
    position: relative;
    background: radial-gradient(ellipse 60% 45% at 50% 50%, var(--stage-glow) 0%, #1a1a1a 60%, var(--stage-dark) 100%);
    font-family: "Arimo", Arial, sans-serif;
  }
  .card { position: absolute; left: 30px; width: 939px; }
  .card-front { top: 50px; height: 535px; background: var(--white); }
  .card-back { top: 608px; height: 537px; background: var(--navy-deep); color: var(--white); }

  .wordmark {
    position: absolute; left: 45px; top: 112px;
    font-weight: 700; font-size: 54px; letter-spacing: -1px; color: var(--navy);
  }
  .person-name {
    position: absolute; left: 45px; top: 297px;
    font-family: "Open Sans", sans-serif; font-weight: 700;
    font-size: 39px; color: var(--navy); letter-spacing: -0.3px;
  }
  .person-role {
    position: absolute; left: 45px; top: 352px;
    font-size: 24px; color: var(--text-grey);
  }
  .licence {
    position: absolute; left: 517px; top: 350px;
    font-size: 24px; color: var(--text-grey);
  }
  .divider {
    position: absolute; left: 0; right: 0; top: 388px; height: 6px;
    background: var(--navy);
  }
  .address {
    position: absolute; left: 45px; top: 426px;
    display: flex; gap: 20px; align-items: flex-start;
    font-size: 24px; line-height: 31px; color: var(--text-grey);
  }
  .address svg { margin-top: 12px; }
  .contacts {
    position: absolute; left: 512px; top: 412px;
    list-style: none; font-size: 23px; line-height: 32px; color: var(--text-grey);
  }
  .contacts li { display: flex; align-items: center; gap: 16px; }
  .contacts svg { width: 24px; height: 24px; flex: none; }

  .services-title {
    position: absolute; left: 0; right: 0; top: 38px; text-align: center;
    font-weight: 700; font-size: 52px;
  }
  .brand-mark {
    position: absolute; left: 95px; top: 120px; width: 250px; height: 250px;
    border-radius: 50%; background: var(--mark-muted);
  }
  .tagline {
    position: absolute; left: 58px; top: 454px;
    font-weight: 700; font-size: 36px;
  }
  .specialties { position: absolute; left: 587px; top: 174px; }
  .specialties h2 { font-size: 38.5px; font-weight: 700; margin-bottom: 6px; }
  .specialties ul { list-style: none; }
  .specialties li {
    display: flex; align-items: center; gap: 35px;
    font-size: 29px; height: 45.5px;
  }
  .specialties li svg { margin-left: 6px; flex: none; }
</style>
</head>
<body>
  <section class="card card-front">
    <div class="wordmark">Kestrel Plumbing</div>
    <div class="person-name">Dale Fenmore</div>
    <div class="person-role">Director</div>
    <div class="licence">Lic: 518604k</div>
    <div class="divider"></div>
    <div class="address">
      <svg width="22" height="37" viewBox="0 0 22 37" aria-hidden="true">
        <path d="M11 0C4.9 0 0 4.9 0 11c0 7.5 11 26 11 26s11-18.5 11-26C22 4.9 17.1 0 11 0zm0 15.5a4.5 4.5 0 1 1 0-9 4.5 4.5 0 0 1 0 9z" fill="var(--navy)"/>
      </svg>
      <p>PO BOX 782<br>Carrowbrook NSW 2179</p>
    </div>
    <ul class="contacts">
      <li>
        <svg viewBox="0 0 24 24" aria-hidden="true"><rect x="5" y="1" width="14" height="22" rx="2.5" fill="var(--navy)"/><rect x="7.5" y="4" width="9" height="14" fill="var(--white)"/></svg>
        0427 596 418
      </li>
      <li>
        <svg viewBox="0 0 24 24" aria-hidden="true"><path d="M1 10l11-8 11 8v12H1z" fill="var(--navy)"/><path d="M1 10l11 7 11-7" fill="none" stroke="var(--white)" stroke-width="1.5"/></svg>
        dale@kestrelplumbing-demo.net.au
      </li>
      <li>
        <svg viewBox="0 0 24 24" aria-hidden="true" fill="none" stroke="var(--navy)" stroke-width="1.5"><circle cx="12" cy="12" r="10"/><ellipse cx="12" cy="12" rx="4.5" ry="10"/><path d="M2 12h20M4 7h16M4 17h16"/></svg>
        www.kestrelplumbing-demo.net.au
      </li>
    </ul>
  </section>

  <section class="card card-back">
    <h1 class="services-title">Mechanical Plumbing Services</h1>
    <div class="brand-mark" role="img" aria-label="Kestrel Plumbing brand mark area"></div>
    <p class="tagline">Kestrel have the Solution</p>
    <div class="specialties">
      <h2>Specialising in:</h2>
      <ul>
        <li><svg width="20" height="14" viewBox="0 0 20 14" aria-hidden="true"><path d="M0 0l9 7-9 7zM10 0l9 7-9 7z" fill="var(--white)"/></svg>Make Good</li>
        <li><svg width="20" height="14" viewBox="0 0 20 14" aria-hidden="true"><path d="M0 0l9 7-9 7zM10 0l9 7-9 7z" fill="var(--white)"/></svg>Refurbishment</li>
        <li><svg width="20" height="14" viewBox="0 0 20 14" aria-hidden="true"><path d="M0 0l9 7-9 7zM10 0l9 7-9 7z" fill="var(--white)"/></svg>Tenancy Fit Out</li>
        <li><svg width="20" height="14" viewBox="0 0 20 14" aria-hidden="true"><path d="M0 0l9 7-9 7zM10 0l9 7-9 7z" fill="var(--white)"/></svg>Plant Room Works</li>
        <li><svg width="20" height="14" viewBox="0 0 20 14" aria-hidden="true"><path d="M0 0l9 7-9 7zM10 0l9 7-9 7z" fill="var(--white)"/></svg>Shut Downs</li>
        <li><svg width="20" height="14" viewBox="0 0 20 14" aria-hidden="true"><path d="M0 0l9 7-9 7zM10 0l9 7-9 7z" fill="var(--white)"/></svg>Change Overs</li>
      </ul>
    </div>
  </section>
</body>
</html>
```